Corvel Lease Homes
will not have subtitle
Corvel Lease Homes -
Creative Brief
Simple
Paul Venner, Tessa Venner
PO Box 58211 20415 #7 Rd Surrey, BC V2T 5K9
info@corvelholdings.ca
www.corvelholdings.ca
On front- white background with small logo and our contact info. Paul's # is 604.555.0187, mine is the other. would like all the colors to be the same as logo and info in blue. Back- blue background with large logo. I would also be interested in simply seeing what you all come up with as you know what looks best-so feel free to do something different than what I said and we'll go from there. Thank you.

```html
<!DOCTYPE html>
<html lang="en">
<head>
<meta charset="utf-8">
<title>Corvel Lease Homes – Stationery</title>
<link rel="stylesheet" href="https://fonts.googleapis.com/css2?family=Cinzel:wght@700&family=Open+Sans:wght@400;600;700&display=swap">
<style>
  :root{
    --stage:#e7e4df;
    --paper:#ffffff;
    --navy:#1c3a86;
    --blue:#2c57b8;
    --deep:#0c1d57;
    --green:#7db544;
    --grey:#8a8f99;
    --rule:#c9ccd3;
    --faint:#e9ecf1;
  }
  *{box-sizing:border-box;margin:0;padding:0}
  html,body{width:1200px;height:554px;overflow:hidden}
  body{background:var(--stage);font-family:"Open Sans",Arial,sans-serif;position:relative;color:var(--navy)}
  .sheet,.envelope,.card{position:absolute;background:var(--paper);box-shadow:0 2px 6px rgba(0,0,0,.18);overflow:hidden}
  .brand{display:flex;align-items:center;justify-content:center;gap:4px;font-family:"Cinzel",Georgia,serif;font-weight:700;color:var(--navy);white-space:nowrap;line-height:1}
  .brand-mark{background:var(--navy);display:inline-block;flex:none}
  .swoosh{position:absolute;left:0;right:0;height:5px;background:linear-gradient(var(--green) 0 2px,transparent 2px 3px,var(--blue) 3px 5px)}
  .footer-text{position:absolute;left:14px;right:14px;display:flex;justify-content:space-between;align-items:flex-start;font-size:4px;line-height:1.4;color:var(--grey);white-space:nowrap}

  /* letterhead and fax */
  .letterhead{left:67px;top:96px;width:290px;height:422px}
  .fax{left:396px;top:96px;width:290px;height:422px}
  .letterhead .brand,.fax .brand{position:absolute;top:22px;left:0;right:0;font-size:11px}
  .letterhead .brand-mark,.fax .brand-mark{width:7px;height:7px}
  .watermark-name{position:absolute;top:200px;left:0;right:0;text-align:center;font-family:"Cinzel",Georgia,serif;font-weight:700;font-size:26px;color:var(--faint)}
  .letterhead .swoosh,.fax .swoosh{bottom:28px}
  .letterhead .footer-text,.fax .footer-text{bottom:10px}

  .fax-title{position:absolute;top:70px;left:20px;font-size:15px;font-weight:700;color:var(--navy)}
  .fax-fields{position:absolute;top:96px;left:20px;right:20px;display:grid;grid-template-columns:1fr 1fr;column-gap:26px;row-gap:8px}
  .fax-field{display:flex;align-items:flex-end;font-size:4.5px;color:var(--grey);border-bottom:1px solid var(--rule);height:11px}
  .fax-options{position:absolute;top:180px;left:20px;right:20px;display:flex;justify-content:space-between;font-size:4.2px;color:var(--grey)}
  .fax-option{display:flex;align-items:center;gap:3px}
  .fax-option::before{content:"";width:5px;height:5px;border:1px solid var(--grey)}

  /* envelopes */
  .envelope-back{left:737px;top:41px;width:391px;height:139px}
  .envelope-back svg{position:absolute;inset:0}
  .envelope-back .brand{position:absolute;top:14px;left:0;right:0;font-size:7px;color:#fff}
  .envelope-back .brand-mark{width:4px;height:4px;background:#fff}
  .envelope-front{left:737px;top:161px;width:391px;height:149px}
  .envelope-front .brand{position:absolute;top:14px;left:14px;font-size:7px;justify-content:flex-start}
  .envelope-front .brand-mark{width:4px;height:4px}
  .return-address{position:absolute;top:25px;left:14px;font-size:4px;color:var(--grey);line-height:1.4}
  .envelope-front .web{position:absolute;right:14px;bottom:12px;font-size:4.5px;color:var(--green)}
  .envelope-front .swoosh{bottom:5px;height:3px;background:linear-gradient(var(--green) 0 1px,transparent 1px 1.5px,var(--blue) 1.5px 3px)}

  /* cards */
  .card-front{width:98px;height:56px}
  .card-back{width:99px;height:48px;background:radial-gradient(ellipse at 50% 45%,var(--blue),var(--deep) 80%)}
  .card-front .brand{position:absolute;top:22px;left:6px;font-size:5.5px;justify-content:flex-start}
  .card-front .brand-mark{width:3.5px;height:3.5px}
  .card-front .person{position:absolute;top:5px;right:6px;text-align:right;font-size:3.4px;color:var(--navy);line-height:1.4}
  .card-front .person b{font-size:4px}
  .card-front .details{position:absolute;bottom:7px;left:6px;font-size:3px;color:var(--grey);line-height:1.4;white-space:nowrap}
  .card-front .swoosh{bottom:2px;height:2px;background:linear-gradient(var(--green) 0 1px,var(--blue) 1px 2px)}
  .card-back .brand{position:absolute;top:20px;left:0;right:0;font-size:6.5px;color:#fff}
  .card-back .brand-mark{width:4px;height:4px;background:#fff}
  .card-1{left:797px;top:353px}
  .card-2{left:943px;top:357px}
  .card-3{left:797px;top:441px}
  .card-4{left:943px;top:449px}
</style>
</head>
<body>

<section class="sheet letterhead">
  <div class="brand"><span class="brand-mark"></span>Corvel Lease Homes</div>
  <div class="watermark-name" aria-hidden="true">Corvel</div>
  <div class="swoosh"></div>
  <div class="footer-text">
    <span>PO Box 58211 20415 #7 Rd<br>Surrey, BC V2T 5K9</span>
    <span>T 604.555.0187<br>F 604.555.0142</span>
    <span>info@corvelholdings.ca</span>
  </div>
</section>

<section class="sheet fax">
  <div class="brand"><span class="brand-mark"></span>Corvel Lease Homes</div>
  <h1 class="fax-title">FAX</h1>
  <div class="fax-fields">
    <div class="fax-field">To:</div><div class="fax-field">From:</div>
    <div class="fax-field">Fax:</div><div class="fax-field">Pages:</div>
    <div class="fax-field">Phone:</div><div class="fax-field">Date:</div>
    <div class="fax-field">Re:</div><div class="fax-field">CC:</div>
  </div>
  <div class="fax-options">
    <span class="fax-option">Urgent</span>
    <span class="fax-option">For Review</span>
    <span class="fax-option">Please Comment</span>
    <span class="fax-option">Please Reply</span>
    <span class="fax-option">Please Recycle</span>
  </div>
  <div class="swoosh"></div>
  <div class="footer-text">
    <span>PO Box 58211 20415 #7 Rd<br>Surrey, BC V2T 5K9</span>
    <span>T 604.555.0187<br>F 604.555.0142</span>
    <span>www.corvelholdings.ca</span>
  </div>
</section>

<section class="envelope envelope-back">
  <svg width="391" height="139" viewBox="0 0 391 139" aria-hidden="true">
    <defs>
      <linearGradient id="flap" x1="0" y1="0" x2="0" y2="1">
        <stop offset="0" stop-color="#2c57b8"/>
        <stop offset="1" stop-color="#0c1d57"/>
      </linearGradient>
    </defs>
    <path d="M0 0H391V30L196 80L0 30Z" fill="url(#flap)"/>
  </svg>
  <div class="brand"><span class="brand-mark"></span>Corvel Lease Homes</div>
</section>

<section class="envelope envelope-front">
  <div class="brand"><span class="brand-mark"></span>Corvel Lease Homes</div>
  <p class="return-address">PO Box 58211 20415 #7 Rd<br>Surrey, BC V2T 5K9</p>
  <span class="web">www.corvelholdings.ca</span>
  <div class="swoosh"></div>
</section>

<section class="card card-front card-1">
  <div class="person"><b>Paul Venner</b><br>604.555.0187</div>
  <div class="brand"><span class="brand-mark"></span>Corvel Lease Homes</div>
  <div class="details">PO Box 58211 20415 #7 Rd, Surrey, BC V2T 5K9<br>info@corvelholdings.ca</div>
  <div class="swoosh"></div>
</section>
<section class="card card-back card-2">
  <div class="brand"><span class="brand-mark"></span>Corvel Lease Homes</div>
</section>
<section class="card card-front card-3">
  <div class="person"><b>Tessa Venner</b><br>604.555.0142</div>
  <div class="brand"><span class="brand-mark"></span>Corvel Lease Homes</div>
  <div class="details">PO Box 58211 20415 #7 Rd, Surrey, BC V2T 5K9<br>www.corvelholdings.ca</div>
  <div class="swoosh"></div>
</section>
<section class="card card-back card-4">
  <div class="brand"><span class="brand-mark"></span>Corvel Lease Homes</div>
</section>

</body>
</html>
```